Heron Home Inspections website

I need a website for a new company called Heron Home Inspections, LLC. based in Northern Virginia. I'd like the site built on the url heroninspections.com and incorporating the graphics that I attached.

Project Deadline Extended
Reason: I got bogged down with my job, with a daughter moving, and with two daughters who are in their final stages of pregnancy. I started this web design job at a really bad time in my life. I do appreciate all of the hard work that the designers have put forth and I will soon make my selection. Thank you, Tim

Target Market(s)

Clarke County, Loudoun County, Fairfax County, Fairfax City, Fauquier County, Arlington County, Arlington City, Frederick County, Shenandoah County

Industry/Entity Type

Home Inspection

Number of Pages Required

1 page

Font styles to use
Sans Serif

Requirements
Must have
• My logo
• Company name: Heron Home Inspections, LLC.
• Tim Rudge, Jr.
• Owner / Principal Inspector
• 703-555-0142
• tim.heroninspections@mailvale.com
• A space to describe me and my business
Should not have
• Please use the color scheme of the uploads that I provided

```html
<!DOCTYPE html>
<html lang="en">
<head>
<meta charset="utf-8">
<title>Heron Home Inspections, LLC</title>
<link href="https://fonts.googleapis.com/css2?family=Roboto:wght@300;400;500&display=swap" rel="stylesheet">
<style>
  :root {
    --navy: #1f2f86;
    --blue: #0b67b8;
    --blue-dark: #0a5aa6;
    --text: #222;
    --muted: #7d7d7d;
    --light: #a5a5a5;
    --rule: #dcdcdc;
    --date: #8a8a8a;
    --footer: #2b2b2b;
    --white: #fff;
  }
  * { margin: 0; padding: 0; box-sizing: border-box; }
  html, body { width: 1200px; height: 1125px; overflow: hidden; background: var(--white); }
  body { font-family: "Roboto", sans-serif; color: var(--text); position: relative; }

  .site-header { position: absolute; left: 0; top: 0; width: 1200px; height: 139px; }
  .brand { position: absolute; left: 99px; top: 30px; display: flex; align-items: center; gap: 10px; color: var(--navy); }
  .brand-mark { width: 44px; height: 44px; border-radius: 50%; background: var(--blue); flex: none; }
  .brand-name { line-height: 1; font-weight: 400; }
  .brand-name .big { display: block; font-size: 32px; letter-spacing: 6px; }
  .brand-name .small { display: block; font-size: 13px; letter-spacing: 1px; margin-top: 6px; }

  .call { position: absolute; right: 100px; top: 26px; display: flex; align-items: center; gap: 8px; }
  .call-text { text-align: right; }
  .call-label { font-size: 12px; color: #555; }
  .call-number { font-size: 19px; color: var(--navy); margin-top: 1px; }
  .call-email { font-size: 11px; color: var(--muted); margin-top: 2px; }
  .call-icon { width: 34px; height: 34px; border: 1px solid #ccc; border-radius: 50%; display: flex; align-items: center; justify-content: center; }

  .main-nav { position: absolute; right: 100px; top: 95px; display: flex; gap: 36px; font-size: 12.5px; }
  .main-nav a { color: #777; text-decoration: none; letter-spacing: .4px; }
  .main-nav a.active { color: var(--navy); }

  .hero { position: absolute; left: 0; top: 139px; width: 1200px; height: 394px; }
  .hero-arrow { position: absolute; top: 180px; width: 27px; height: 34px; display: flex; align-items: center; justify-content: center; }
  .hero-arrow.prev { left: 0; background: rgba(255,255,255,.25); }
  .hero-arrow.next { right: 0; background: var(--blue-dark); }

  .booking { position: absolute; left: 99px; top: 576px; width: 242px; height: 236px; background: linear-gradient(#1279c8, #0a5aa6); padding: 18px; }
  .booking h2 { font-weight: 400; color: var(--white); font-size: 18px; margin-bottom: 13px; white-space: nowrap; }
  .field { height: 34px; background: var(--white); border-radius: 3px; margin-bottom: 9px; font-size: 12px; color: #444; padding: 10px 12px; }
  .submit { display: inline-block; background: linear-gradient(#7ccbf5, #4db0ea); color: var(--white); font-size: 12px; font-weight: 500; padding: 7px 11px; border-radius: 3px; margin-top: 1px; }

  .badges { position: absolute; left: 99px; top: 838px; display: flex; align-items: center; gap: 18px; }
  .badge-round { width: 70px; height: 70px; border-radius: 50%; background: #111; }
  .badge-wide { width: 126px; height: 48px; border-radius: 24px; background: #5a4aa0; opacity: .85; }

  .social { position: absolute; left: 99px; top: 934px; display: flex; gap: 11px; }
  .social span { width: 26px; height: 26px; border-radius: 50%; }

  .welcome { position: absolute; left: 365px; top: 573px; width: 737px; }
  h1 { font-weight: 400; color: var(--navy); font-size: 23px; margin-bottom: 14px; }
  .lead { font-size: 13px; font-weight: 500; line-height: 19px; color: var(--text); margin-bottom: 9px; }
  .intro { font-size: 11px; line-height: 20.5px; color: var(--muted); }
  .divider { position: absolute; left: 365px; top: 745px; width: 737px; height: 1px; background: var(--rule); }

  .col h2 { font-weight: 400; color: var(--navy); font-size: 23px; }
  .why { position: absolute; left: 365px; top: 770px; width: 292px; }
  .why-body { display: flex; gap: 11px; margin-top: 16px; }
  .why-photo { width: 95px; height: 176px; flex: none; background: linear-gradient(160deg, #c9b16a, #6f6a52 45%, #3d5070); }
  .why p { font-size: 11px; line-height: 20.6px; color: var(--muted); margin-top: -4px; }
  .col-rule { position: absolute; left: 702px; top: 775px; width: 1px; height: 213px; background: var(--rule); }

  .news { position: absolute; left: 747px; top: 770px; width: 355px; }
  .news-item { display: flex; gap: 12px; margin-top: 24px; }
  .news-item + .news-item { margin-top: 28px; }
  .date { width: 37px; height: 50px; background: var(--date); color: var(--white); text-align: center; flex: none; padding-top: 6px; }
  .date .m { font-size: 11px; display: block; }
  .date .d { font-size: 19px; display: block; line-height: 21px; }
  .news-item h3 { font-size: 13px; font-weight: 400; color: var(--text); margin-top: -3px; margin-bottom: 4px; }
  .news-item p { font-size: 11px; line-height: 17px; color: var(--light); }

  .site-footer { position: absolute; left: 0; top: 1039px; width: 1200px; height: 86px; background: var(--footer); color: #ddd; text-align: center; font-size: 11px; }
  .footer-nav { margin-top: 23px; }
  .footer-nav .sep { margin: 0 8px; }
  .copyright { margin-top: 14px; }
</style>
</head>
<body>
  <header class="site-header">
    <div class="brand">
      <span class="brand-mark"></span>
      <div class="brand-name">
        <span class="big">HERON</span>
        <span class="small">Home Inspections, LLC</span>
      </div>
    </div>
    <div class="call">
      <div class="call-text">
        <div class="call-label">Call us</div>
        <div class="call-number">703-555-0142</div>
        <div class="call-email">tim.heroninspections@mailvale.com</div>
      </div>
      <div class="call-icon">
        <svg width="14" height="14" viewBox="0 0 24 24"><path d="M6.6 10.8a15 15 0 006.6 6.6l2.2-2.2a1 1 0 011-.25 11.4 11.4 0 003.6.57 1 1 0 011 1V20a1 1 0 01-1 1A17 17 0 013 4a1 1 0 011-1h3.5a1 1 0 011 1c0 1.25.2 2.45.57 3.57a1 1 0 01-.25 1z" fill="#999"/></svg>
      </div>
    </div>
    <nav class="main-nav">
      <a class="active" href="#">HOME</a>
      <a href="#">ABOUT US</a>
      <a href="#">SERVICES</a>
      <a href="#">CONTACT US</a>
    </nav>
  </header>

  <section class="hero">
    <svg width="1200" height="394" viewBox="0 0 1200 394">
      <defs>
        <linearGradient id="sky" x1="0" y1="0" x2="0" y2="1">
          <stop offset="0" stop-color="#3f8fd6"/>
          <stop offset=".45" stop-color="#9cc4e6"/>
          <stop offset=".55" stop-color="#8e9c84"/>
          <stop offset="1" stop-color="#6f7b66"/>
        </linearGradient>
        <linearGradient id="side" x1="0" y1="0" x2="0" y2="1">
          <stop offset="0" stop-color="#f1f1f1"/>
          <stop offset=".5" stop-color="#a9a9a6"/>
          <stop offset="1" stop-color="#5c6a4d"/>
        </linearGradient>
      </defs>
      <rect x="0" y="0" width="1200" height="394" fill="var(--blue)"/>
      <polygon points="0,0 200,0 360,196 195,394 0,394" fill="#fff"/>
      <g role="img" aria-label="Photo of a two-storey house viewed through a magnifying glass">
        <polygon points="0,40 180,40 338,196 185,394 0,394" fill="url(#side)"/>
      </g>
      <polygon points="216,8 1200,8 1200,385 230,385 366,196" fill="#fff"/>
      <g role="img" aria-label="Photo of a large sage-green colonial house with white columns under a blue sky">
        <polygon points="232,8 1200,8 1200,385 240,385 372,196" fill="url(#sky)"/>
      </g>
    </svg>
    <div class="hero-arrow prev"><svg width="10" height="18" viewBox="0 0 10 18"><path d="M9 1L1 9l8 8" stroke="#fff" fill="none" stroke-width="1.5"/></svg></div>
    <div class="hero-arrow next"><svg width="10" height="18" viewBox="0 0 10 18"><path d="M1 1l8 8-8 8" stroke="#fff" fill="none" stroke-width="1.5"/></svg></div>
  </section>

  <aside class="booking">
    <h2>Book a Inspections Now</h2>
    <div class="field">City</div>
    <div class="field">State</div>
    <div class="field">Zip code</div>
    <span class="submit">Submit</span>
  </aside>

  <div class="badges">
    <span class="badge-round"></span>
    <span class="badge-wide"></span>
  </div>

  <div class="social">
    <span style="background:#3b5998"></span>
    <span style="background:#1da1f2"></span>
    <span style="background:#1b86b8"></span>
  </div>

  <section class="welcome">
    <h1>Welcome to Heron Home Inspections, LLC</h1>
    <p class="lead">Owner, Tim Rudge is a trained builder with experience in new construction, as well as remodeling, HVAC systems, framing, roofing, siding, and masonry.</p>
    <p class="intro">For most families, a home purchase is the largest investment that they will make in a lifetime. The decision to purchase a home should be based on a thorough review of its systems and overall condition to ensure that their investment is one based research and fact. A good home inspector will give you the research based facts that help a buyer to make the best possible decision in a home purchase.</p>
  </section>
  <div class="divider"></div>

  <section class="col why">
    <h2>Why use Heron Inspections</h2>
    <div class="why-body">
      <div class="why-photo" role="img" aria-label="Photo of the inspector in a hard hat holding a clipboard"></div>
      <p>I am a 20 year Navy veteran trained and devoted to being thorough in my inspection procedures and comprehensive in my documentation. Whether you are buying your forever home or one that you plan to have for a few years and then move on, protect your investment by knowing what you are buying before going to closing.</p>
    </div>
  </section>
  <div class="col-rule"></div>

  <section class="col news">
    <h2>Latest News</h2>
    <article class="news-item">
      <div class="date"><span class="m">Jun</span><span class="d">25</span></div>
      <div>
        <h3>Curabitur aliquam, sapien id vehicula ultricies.</h3>
        <p>Phasellus et tempus nisl, at tristique tortor. Curabitur quis elit neque. Nullam eu viverra sapien, ut gravida nunc. Etiam ac libero malesuada diam semper lacinia.</p>
      </div>
    </article>
    <article class="news-item">
      <div class="date"><span class="m">Jun</span><span class="d">25</span></div>
      <div>
        <h3>Curabitur aliquam, sapien id vehicula ultricies.</h3>
        <p>Phasellus et tempus nisl, at tristique tortor. Curabitur quis elit neque. Nullam eu viverra sapien, ut gravida nunc. Etiam ac libero malesuada diam semper lacinia.</p>
      </div>
    </article>
  </section>

  <footer class="site-footer">
    <div class="footer-nav">Home<span class="sep">|</span>About us<span class="sep">|</span>Services<span class="sep">|</span>Contact us</div>
    <div class="copyright">Copyright &copy; 2015 Heron Inspections. &nbsp;All rights reserved.</div>
  </footer>
</body>
</html>
```